Byte Crew - Settle Inn

A flyer to promote a service by Byte Crew that provides IT set up in home when moving house.

It should be for print format (A4, A5 and an email friendly version)

Logos, previous flyer, image all attached.

Please use black, green and white as base colours.Please change boys sweater/jumper in the photo to green to match the logo.

Byte Crew are bring a helpdesk to your front door, saving you time and money. With a variety of packages to suit your needs, the Byte Crew aims to tackle both small and complex issues from setting up a home network to servicing the needs of a growing company.

Target Market(s)

Consumers moving house, Relocation agents, Real Estate agents

Requirements
Must have
• Logo, image, text all attached
• Use of green, black and white
Nice to have
• Also have coloured ties if you want them for design

```html
<!DOCTYPE html>
<html lang="en">
<head>
<meta charset="utf-8">
<title>Byte Crew – Settle Inn</title>
<link rel="stylesheet" href="https://fonts.googleapis.com/css2?family=Bangers&family=Montserrat:wght@700;800;900&display=swap">
<style>
  :root {
    --stage: #ececec;
    --black: #0b0d0b;
    --board-dark: #0f2a12;
    --board-mid: #1f4d22;
    --board-light: #2f6b2c;
    --green: #8ee31c;
    --green-deep: #5cb512;
    --white: #ffffff;
    --photo-a: #a9b3a0;
    --photo-b: #5b7a48;
    --photo-c: #d9c2ad;
  }
  * { box-sizing: border-box; margin: 0; padding: 0; }
  html, body { width: 1200px; height: 848px; overflow: hidden; background: var(--stage); }
  .canvas { position: relative; width: 1200px; height: 848px; }

  .flyer {
    position: absolute; left: 356px; top: 53px; width: 488px; height: 690px;
    overflow: hidden;
    border: 3px solid #1d3a1d;
    background: radial-gradient(ellipse at 50% 55%, var(--board-light) 0%, var(--board-mid) 45%, var(--board-dark) 100%);
    font-family: "Montserrat", sans-serif;
    color: var(--white);
    box-shadow: 0 6px 14px rgba(0,0,0,.35);
  }

  .top-band {
    position: absolute; left: 0; top: 0; width: 100%; height: 118px;
    background: var(--black);
  }
  .dash {
    position: absolute; left: 0; width: 100%;
    border-top: 1.5px dashed rgba(255,255,255,.55);
  }
  .dash--top { top: 112px; transform: rotate(-3.2deg); }
  .dash--mid { top: 178px; transform: rotate(-3.2deg); }
  .dash--foot-a { left: -10px; width: 520px; top: 614px; transform: rotate(-4deg); }
  .dash--foot-b { left: -10px; width: 520px; top: 672px; transform: rotate(-4deg); }

  .headline {
    position: absolute; left: 24px; top: 24px;
    font-family: "Bangers", sans-serif; font-size: 34px; line-height: 30px;
    letter-spacing: 1px; color: var(--green);
    transform: rotate(-3.2deg); transform-origin: left top;
    text-shadow: 2px 2px 0 #000;
  }

  .intro {
    position: absolute; left: 26px; top: 118px; width: 340px;
    font-size: 11.5px; font-weight: 800; line-height: 14px;
    text-transform: uppercase; text-align: right;
    transform: rotate(-3.2deg); transform-origin: left top;
  }

  .hero-photo { position: absolute; left: -10px; top: 140px; width: 510px; height: 300px; }

  .package {
    position: absolute; left: 30px; top: 248px;
    font-family: "Montserrat", sans-serif; font-weight: 900; font-size: 29px; line-height: 28px;
    text-transform: uppercase; color: var(--white);
    transform: rotate(-4deg); transform-origin: left top;
    text-shadow: 2px 2px 0 #000;
  }
  .package__price {
    position: absolute; left: 108px; top: 36px;
    font-family: "Bangers", sans-serif; font-size: 40px; color: var(--green);
    letter-spacing: 1px;
  }

  .features {
    position: absolute; left: 167px; top: 412px; width: 300px;
    list-style: none;
    font-size: 7.5px; font-weight: 800; line-height: 9px;
    text-transform: uppercase;
    transform: rotate(-4deg); transform-origin: left top;
  }
  .features li { position: relative; padding-left: 13px; margin-bottom: 3px; }
  .features li::before {
    content: ""; position: absolute; left: 0; top: 1px;
    width: 7px; height: 7px; border-radius: 50%; background: var(--green);
  }

  .green-rule {
    position: absolute; left: -10px; top: 602px; width: 520px; height: 3px;
    background: var(--green); transform: rotate(-4deg); transform-origin: left top;
  }
  .foot-band {
    position: absolute; left: -10px; top: 606px; width: 540px; height: 140px;
    background: var(--black); transform: rotate(-4deg); transform-origin: left top;
  }

  .book-now { position: absolute; left: 22px; top: 470px; width: 136px; height: 136px; z-index: 2; }

  .contact {
    position: absolute; left: 58px; top: 628px;
    font-size: 13px; font-weight: 800; line-height: 17px; font-style: normal;
    text-transform: uppercase;
    transform: rotate(-4deg); transform-origin: left top;
  }
  .brand {
    position: absolute; left: 326px; top: 602px;
    display: flex; align-items: center; gap: 6px;
    font-family: "Montserrat", sans-serif; font-weight: 800; font-size: 20px;
    color: var(--white);
    transform: rotate(-4deg); transform-origin: left top;
  }
  .brand__mark { width: 10px; height: 10px; background: var(--green); }
</style>
</head>
<body>
<div class="canvas">
  <article class="flyer">
    <div class="top-band"></div>

    <svg class="hero-photo" viewBox="0 0 510 300" role="img" aria-label="Photo of a startled boy in large black glasses and a green jumper holding a network cable">
      <defs>
        <radialGradient id="photoTone" cx="55%" cy="45%" r="60%">
          <stop offset="0%" stop-color="var(--photo-c)"/>
          <stop offset="45%" stop-color="var(--photo-a)"/>
          <stop offset="100%" stop-color="var(--photo-b)"/>
        </radialGradient>
      </defs>
      <ellipse cx="262" cy="148" rx="262" ry="140" fill="#0b0d0b"/>
      <ellipse cx="262" cy="148" rx="254" ry="134" fill="url(#photoTone)"/>
    </svg>

    <div class="dash dash--top"></div>
    <div class="dash dash--mid"></div>

    <h1 class="headline">Can't remember<br>what to plug in where?</h1>

    <p class="intro">Do not fear, the Byte Crew is here!<br>We take all the pain out of moving house<br>and get you set-up, online and connected<br>before you can say the word geek..</p>

    <h2 class="package">Welcome<br>Home<br>Crew<span class="package__price">$425</span></h2>

    <ul class="features">
      <li>Pre-visit online assessment to ensure maximum use of our crew's time</li>
      <li>Ready: IT health check and audit report</li>
      <li>Set: connection of your wireless network for user access including passwords and parental control if desired</li>
      <li>Go: set up of 3 computers and 1 printer</li>
      <li>Expanding the family: connection of one additional device eg Stream Box, Tab Pad, Play Cube, Smart TV*</li>
      <li>Updating of software and virus security check</li>
      <li>Byte Crew membership</li>
      <li>Includes travel cost and up to 4 hours of a crew member's time in your house</li>
      <li>1 month free on Crew@Home packages**</li>
      <li>Awesome Byte Crew fridge magnet</li>
    </ul>

    <div class="green-rule"></div>
    <div class="foot-band"></div>
    <div class="dash dash--foot-a"></div>
    <div class="dash dash--foot-b"></div>

    <svg class="book-now" viewBox="0 0 140 140" aria-label="Book now">
      <polygon fill="#ffffff" stroke="#0b0d0b" stroke-width="3"
        points="70,4 80,24 100,10 102,33 126,28 116,50 138,60 118,74 134,94 110,98 116,122 94,114 86,136 70,120 54,136 46,114 24,122 30,98 6,94 22,74 2,60 24,50 14,28 38,33 40,10 60,24"/>
      <circle cx="70" cy="70" r="42" fill="#0b0d0b"/>
      <g transform="rotate(-10 70 70)" font-family="Bangers, sans-serif" fill="#8ee31c" text-anchor="middle">
        <text x="70" y="66" font-size="28">BOOK</text>
        <text x="70" y="92" font-size="28">NOW!</text>
      </g>
      <rect x="40" y="102" width="62" height="4" fill="#8ee31c" transform="rotate(-10 70 104)"/>
    </svg>

    <address class="contact">
      www.bytecrew.asia<br>
      Email booking@bytecrew.asia<br>
      Hotline 6120 4471
    </address>

    <div class="brand"><span class="brand__mark"></span>Byte Crew</div>
  </article>
</div>
</body>
</html>
```